Machining Business Order Thank You Insert

I am looking for a business style card to include with orders that I ship. The card needs to thank the recipient for their order, and encourage them to leave a review. The card should include my business name and contact information and have an area to hand write a message.

I mainly sale on Craftory and my own website. We are a machining an manufacturing business that are in the sale of mostly metal machined and 3d printed plastic products.

The front of the card should include the following:
Logo: (attached)
Instagram: https://www.instagram.com/kelvorn/
Facebook: https://www.facebook.com/Kelvorn
Website: https://www.kelvorn-example.com/

The back of the card needs an area to write a message

Industry/Entity Type

3D Printing, Machining, Craftory

Contact Information for Business Card

Black or white front, white back to write a personal message

Font styles to use
Sans Serif

Colors

Designer to choose colors to be used in the design.

Requirements
Must have
• Encourage a review, social media info

```html
<!DOCTYPE html>
<html lang="en">
<head>
<meta charset="utf-8">
<title>Kelvorn – Thank You Card</title>
<link rel="stylesheet" href="https://fonts.googleapis.com/css2?family=Open+Sans:wght@300;400;600&family=Rajdhani:wght@500;600&family=Arimo:wght@400&display=swap">
<style>
  :root {
    --orange: #ff3d0f;
    --black: #000000;
    --ink: #1c1c1c;
    --grey: #555555;
    --rule-grey: #bdbdbd;
    --light: #e2e2e2;
    --paper: #ffffff;
    --page: #ffffff;
  }
  * { margin: 0; padding: 0; box-sizing: border-box; }
  html, body { width: 1200px; height: 1200px; overflow: hidden; background: var(--page); }
  body { position: relative; font-family: "Open Sans", Arial, sans-serif; color: var(--ink); }

  .card { position: absolute; left: 161px; width: 857px; }
  .card-front { top: 36px; height: 488px; background: var(--black); }
  .card-back { top: 548px; height: 614px; background: var(--paper); box-shadow: 0 0 0 1px #eeeeee; }

  /* Front */
  .social { position: absolute; top: 55px; display: flex; align-items: center; gap: 11px; color: #fff; font-size: 24px; }
  .social-mark { width: 31px; height: 31px; border-radius: 5px; background: var(--orange); }
  .social-instagram { left: 55px; }
  .social-facebook { left: 639px; }

  .thanks-title { position: absolute; left: 0; right: 0; top: 140px; text-align: center; font-family: "Rajdhani", Arial, sans-serif; font-weight: 600; font-size: 44px; letter-spacing: 0.12em; color: #fff; }
  .thanks-rule { position: absolute; left: 378px; width: 100px; top: 206px; height: 3px; background: var(--orange); }
  .review-prompt { position: absolute; left: 0; right: 0; top: 228px; text-align: center; font-size: 20px; font-weight: 300; line-height: 1.45; color: var(--light); }
  .review-prompt strong { font-weight: 600; color: var(--orange); }

  .brand-name { font-family: "Rajdhani", Arial, sans-serif; font-weight: 500; letter-spacing: 0.28em; color: var(--orange); }
  .front-brand { position: absolute; left: 0; right: 0; top: 326px; text-align: center; font-size: 54px; line-height: 1; padding-left: 0.28em; }
  .front-url { position: absolute; left: 0; right: 0; top: 408px; text-align: center; font-size: 30px; font-weight: 300; color: var(--light); letter-spacing: 0.01em; }

  /* Back */
  .services-title { position: absolute; left: 0; right: 0; top: 24px; text-align: center; font-size: 34px; font-weight: 600; color: var(--ink); }
  .services-rule { position: absolute; left: 349px; width: 157px; top: 72px; height: 3px; background: var(--orange); }
  .service { position: absolute; top: 101px; }
  .service-cnc { left: 45px; width: 245px; }
  .service-print { left: 321px; width: 232px; }
  .service-design { left: 577px; width: 240px; }
  .service h3 { font-size: 16.5px; font-weight: 600; margin-bottom: 7px; white-space: nowrap; }
  .service p { font-size: 10px; font-weight: 600; line-height: 1.3; color: var(--ink); }
  .service ul { margin-top: 8px; padding-left: 45px; font-size: 10.5px; line-height: 1.5; }
  .service-print ul, .service-design ul { padding-left: 24px; margin-top: 6px; }
  .divider { position: absolute; top: 100px; width: 2px; height: 141px; background: var(--orange); }
  .divider-1 { left: 300px; }
  .divider-2 { left: 562px; }

  .note-area { position: absolute; left: 45px; right: 45px; top: 262px; height: 104px; }
  .note-label { font-size: 14px; font-weight: 600; color: var(--orange); letter-spacing: 0.04em; }
  .note-line { position: absolute; left: 0; right: 0; height: 1px; background: var(--rule-grey); }
  .note-line-1 { top: 48px; }
  .note-line-2 { top: 84px; }

  .person-name { position: absolute; left: 37px; top: 392px; font-size: 31px; font-weight: 400; color: var(--ink); }
  .person-role { position: absolute; left: 37px; top: 430px; font-size: 19px; }
  .name-rule { position: absolute; left: 97px; width: 708px; top: 442px; height: 2px; background: var(--orange); }

  .back-brand { position: absolute; left: 460px; top: 395px; display: flex; align-items: center; gap: 40px; }
  .back-brand-mark { width: 34px; height: 34px; background: var(--orange); }
  .back-brand .brand-name { font-size: 24px; }

  .contact { position: absolute; display: flex; align-items: center; font-family: "Arimo", Arial, sans-serif; font-size: 21.5px; letter-spacing: 0.03em; color: var(--ink); }
  .contact svg { width: 26px; height: 26px; fill: var(--orange); margin-right: 16px; }
  .contact-phone { left: 44px; top: 486px; }
  .contact-email { left: 44px; top: 538px; }
  .contact-web { left: 461px; top: 486px; }
  .contact-address { left: 461px; top: 536px; }

  .band { position: absolute; bottom: 0; height: 17px; }
  .band-orange { left: 0; width: 427px; background: var(--orange); }
  .band-grey { left: 427px; right: 0; background: var(--grey); }
</style>
</head>
<body>

<section class="card card-front">
  <div class="social social-instagram"><span class="social-mark"></span>kelvorn</div>
  <div class="social social-facebook"><span class="social-mark"></span>Kelvorn</div>
  <h1 class="thanks-title">THANK YOU FOR YOUR ORDER</h1>
  <div class="thanks-rule"></div>
  <p class="review-prompt">Enjoying your parts? Please leave us a review on <strong>Craftory</strong><br>and follow us for new projects.</p>
  <div class="brand-name front-brand">KELVORN</div>
  <div class="front-url">www.kelvorn-example.com</div>
</section>

<section class="card card-back">
  <h2 class="services-title">SERVICES</h2>
  <div class="services-rule"></div>

  <div class="service service-cnc">
    <h3>CNC Machining / Fabrication</h3>
    <p>We are capable of performing a variety of manufacturing methods to produce parts to meet your needs.</p>
    <ul><li>3 Axis CNC Milling</li><li>CNC Turning</li><li>Welding</li><li>Tumble Finishing</li></ul>
  </div>
  <div class="divider divider-1"></div>
  <div class="service service-print">
    <h3>3D Printing</h3>
    <p>Our 3D print capabilities allow us to make low cost prototype parts or parts for personal use. A variety of materials are available depending on application.</p>
    <ul><li>FFF Printing</li><li>SLA Printing</li></ul>
  </div>
  <div class="divider divider-2"></div>
  <div class="service service-design">
    <h3>2D / 3D Design &amp; Engineering</h3>
    <p>We can transform your idea or sketch into a 3D model or drawing ready for manufacturing.</p>
    <ul><li>3D Modeling</li><li>2D Drawing</li><li>Rendering</li></ul>
  </div>

  <div class="note-area">
    <div class="note-label">A PERSONAL NOTE</div>
    <div class="note-line note-line-1"></div>
    <div class="note-line note-line-2"></div>
  </div>

  <div class="person-name">YOUR NAME</div>
  <div class="person-role">CEO</div>
  <div class="name-rule"></div>

  <div class="back-brand"><span class="back-brand-mark"></span><span class="brand-name">KELVORN</span></div>

  <div class="contact contact-phone">
    <svg viewBox="0 0 24 24"><path d="M6.6 10.8a15.1 15.1 0 0 0 6.6 6.6l2.2-2.2c.3-.3.7-.4 1-.2 1.1.4 2.3.6 3.6.6.6 0 1 .4 1 1V20c0 .6-.4 1-1 1A17 17 0 0 1 3 4c0-.6.4-1 1-1h3.5c.6 0 1 .4 1 1 0 1.3.2 2.5.6 3.6.1.3 0 .7-.2 1z"/></svg>
    01+2345 6789 0123
  </div>
  <div class="contact contact-email">
    <svg viewBox="0 0 24 24"><path d="M1 5h22v14H1z M2.5 6.5 12 13l9.5-6.5" fill="var(--orange)" stroke="#fff" stroke-width="1.6"/></svg>
    info@company.com
  </div>
  <div class="contact contact-web">
    <svg viewBox="0 0 24 24"><circle cx="12" cy="12" r="10.5"/><path d="M1.5 12h21M12 1.5v21M12 1.5c-3.5 3-3.5 18 0 21M12 1.5c3.5 3 3.5 18 0 21M3.5 6.5h17M3.5 17.5h17" stroke="#fff" stroke-width="1.3" fill="none"/></svg>
    www.kelvorn-example.com
  </div>
  <div class="contact contact-address">
    <svg viewBox="0 0 24 24"><path d="M12 1a7 7 0 0 0-7 7c0 5 7 11.5 7 11.5S19 13 19 8a7 7 0 0 0-7-7zm0 9.5A2.5 2.5 0 1 1 12 5.5a2.5 2.5 0 0 1 0 5z"/><rect x="5" y="21.5" width="14" height="1.8"/></svg>
    Street Loation,state,country
  </div>

  <div class="band band-orange"></div>
  <div class="band band-grey"></div>
</section>

</body>
</html>
```